Workplace Safety Consultancy Business needs business card design

We need a business card for a new business providing workplace health and safety consulting called 'Worksure Path'. We will be providing small to medium sized businesses assistance with OH&S and HR matters to ensure that their employees and the public are safe in the workplace and that they are meeting their legislative requirements. Would like to see the words 'practical workplace safety solutions' on the card. Personal details on the back. It needs to be clean, smart and professional (no fluff). Would like to see a simple logo if possible as well. Have been looking at orange and black, but open to other ideas.
Updates
Thank you to those to have created designs for us so far! We are really impressed with the impact of the black and orange having now seen it. Would be great if any further designs used those colours. Cheers.

Thank you to everyone that submitted a design. Your work is of the highest quality and we had a hard decision deciding. Sorry if we didn't choose your design, but it just came down to the one that stood out to us personally. Cheers.

Target Market(s)
Small-Medium business owners in Queensland, Australia. Age 25-60 male and female. Initially targeting those in the trade type industries
Industry/Entity Type
Health
Look and feel
Each slider illustrates characteristics of the customer's brand and the style your logo design should communicate.

```html
<!DOCTYPE html>
<html lang="en">
<head>
<meta charset="utf-8">
<title>Worksure Path – Business Card</title>
<link rel="stylesheet" href="https://fonts.googleapis.com/css2?family=Jost:wght@400&family=EB+Garamond:wght@400&family=Open+Sans:wght@400&display=swap">
<style>
  :root {
    --stage: #4a4a4a;
    --card-light: #fbfbfb;
    --card-mid: #e4e4e4;
    --card-edge: #c9c9c9;
    --brand-orange: #f26b0a;
    --ink: #111111;
    --ink-soft: #3a3a3a;
    --rule: #9a9a9a;
    --helmet-pale: #f6d27a;
    --helmet-fade: rgba(246, 210, 122, 0);
  }
  * { margin: 0; padding: 0; box-sizing: border-box; }
  html, body {
    width: 1200px; height: 358px; overflow: hidden;
    background: var(--stage);
  }
  .stage { position: relative; width: 1200px; height: 358px; }

  .card {
    position: absolute; top: 29px;
    width: 526px; height: 301px;
    overflow: hidden;
    background: radial-gradient(ellipse 70% 80% at 55% 30%, var(--card-light) 0%, var(--card-mid) 60%, var(--card-edge) 100%);
  }
  .card--front { left: 35px; }
  .card--back { left: 638px; }

  .brand-mark {
    position: absolute; border-radius: 50%;
    background: var(--brand-orange);
  }
  .brand-name {
    position: absolute; white-space: nowrap;
    font-family: "Jost", sans-serif; font-weight: 400;
    color: var(--brand-orange);
  }
  .brand-rule {
    position: absolute; height: 0;
    border-top: 1px dotted var(--rule);
  }
  .tagline {
    position: absolute; white-space: nowrap;
    font-family: "EB Garamond", serif; color: var(--ink-soft);
  }

  /* Front */
  .card--front .brand-mark { left: 228px; top: 70px; width: 70px; height: 70px; }
  .card--front .brand-name { left: 0; width: 526px; text-align: center; top: 162px; font-size: 33px; letter-spacing: 0.5px; }
  .card--front .brand-rule { left: 165px; width: 192px; top: 206px; }
  .card--front .tagline { left: 0; width: 526px; text-align: center; top: 210px; font-size: 14px; }

  /* Back */
  .card--back .brand-mark { left: 40px; top: 34px; width: 44px; height: 44px; }
  .card--back .brand-name { left: 28px; top: 90px; font-size: 19px; }
  .card--back .brand-rule { left: 30px; width: 106px; top: 114px; }
  .card--back .tagline { left: 30px; top: 115px; font-size: 8.5px; }

  .helmet-art {
    position: absolute; left: 300px; top: 60px;
    width: 260px; height: 230px;
    border-radius: 50% 40% 10% 10%;
    background: radial-gradient(ellipse at 45% 40%, var(--helmet-pale) 0%, rgba(246,210,122,0.6) 55%, var(--helmet-fade) 100%);
  }

  .person { position: absolute; left: 39px; top: 150px; font-family: "Open Sans", sans-serif; color: var(--ink); }
  .person-name { font-size: 16px; line-height: 20px; }
  .person-role { font-size: 10px; line-height: 12px; margin-left: 2px; }

  .contact {
    position: absolute; left: 39px; top: 207px;
    list-style: none;
    font-family: "Open Sans", sans-serif; font-size: 11.5px; line-height: 16px;
    color: var(--ink);
  }
</style>
</head>
<body>
<main class="stage">
  <section class="card card--front" aria-label="Card front">
    <span class="brand-mark" aria-hidden="true"></span>
    <h1 class="brand-name">Worksure Path</h1>
    <span class="brand-rule" aria-hidden="true"></span>
    <p class="tagline">practical workplace safety solutions</p>
  </section>

  <section class="card card--back" aria-label="Card back">
    <div class="helmet-art" role="img" aria-label="Large faded yellow safety helmet illustration"></div>
    <span class="brand-mark" aria-hidden="true"></span>
    <p class="brand-name">Worksure Path</p>
    <span class="brand-rule" aria-hidden="true"></span>
    <p class="tagline">practical workplace safety solutions</p>

    <div class="person">
      <p class="person-name">Your Name</p>
      <p class="person-role">managing director</p>
    </div>

    <ul class="contact">
      <li>PO box - 48 219&nbsp;&nbsp; Worksure Path</li>
      <li>Corner Kelso 1233, Australia</li>
      <li>Phone - +61 700 555 019</li>
      <li>Email - yourname@worksurepath.info</li>
    </ul>
  </section>
</main>
</body>
</html>
```